Velmora Builders LLC- Bus. Cards, Door Hangers, Invoice, Estimates, Postcards
I want a proffessional package that express who we are and what we do. www.velmora-builders.example
Velmora Builders LLC- Bus. Cards, Door Hangers, Invoice, Estimates, Postcards - Construction
Creative Brief
Professional
Calvin Tressel
Owner
4216 Pellham Ave. Denver, CO. 80417
calvin@velmora-builders.example
www.velmora-builders.example
Spray Foam Insulation Energy Auditing Weatherization Thermal Imaging

```html
<!DOCTYPE html>
<html lang="en">
<head>
<meta charset="UTF-8">
<title>Velmora Builders – Business Card</title>
<link rel="stylesheet" href="https://fonts.googleapis.com/css2?family=Nunito+Sans:wght@600;800&display=swap">
<style>
  :root {
    --brand-green: #00a651;
    --paper: #ffffff;
    --ink-light: #ffffff;
  }
  html, body {
    margin: 0;
    padding: 0;
    width: 1200px;
    height: 967px;
    overflow: hidden;
    background: var(--paper);
    font-family: "Nunito Sans", Arial, sans-serif;
  }
  .card {
    position: absolute;
    left: 36px;
    top: 143px;
    width: 1128px;
    height: 678px;
  }
  .card__brand-band {
    position: absolute;
    left: 0; top: 0;
    width: 100%;
    height: 273px;
    background: var(--brand-green);
  }
  .card__name-strip {
    position: absolute;
    left: 0; top: 273px;
    width: 100%;
    height: 65px;
    background: var(--paper);
  }
  .card__contact-band {
    position: absolute;
    left: 0; top: 338px;
    width: 100%;
    height: 340px;
    background: var(--brand-green);
  }
  .brand-name {
    position: absolute;
    left: 89px;
    top: 164px;
    margin: 0;
    font-size: 74px;
    font-weight: 600;
    letter-spacing: -1px;
    line-height: 1;
    color: var(--ink-light);
  }
  .person {
    position: absolute;
    left: 89px;
    top: 285px;
    margin: 0;
    line-height: 1;
    color: var(--brand-green);
  }
  .person__name {
    font-size: 46px;
    font-weight: 800;
  }
  .person__role {
    font-size: 22px;
    font-weight: 800;
    margin-left: 10px;
  }
  .contact {
    position: absolute;
    left: 89px;
    margin: 0;
    color: var(--ink-light);
    font-size: 31px;
    font-weight: 800;
    line-height: 39px;
  }
  .contact--address { top: 365px; }
  .contact--reach { top: 487px; }
  .divider {
    position: absolute;
    left: 89px;
    top: 459px;
    width: 953px;
    height: 6px;
    background: var(--ink-light);
  }
</style>
</head>
<body>
  <section class="card" aria-label="Velmora Builders business card">
    <div class="card__brand-band"></div>
    <div class="card__name-strip"></div>
    <div class="card__contact-band"></div>

    <h1 class="brand-name">Velmora Builders</h1>

    <p class="person">
      <span class="person__name">Calvin Tressel</span><span class="person__role">– Owner</span>
    </p>

    <address class="contact contact--address" style="font-style:normal">
      4216 Pellham Ave.<br>
      Denver, CO. 80417
    </address>

    <div class="divider"></div>

    <p class="contact contact--reach">
      631-555-0148<br>
      calvin@velmora-builders.example<br>
      www.velmora-builders.example
    </p>
  </section>
</body>
</html>
```